New website design for small car detailing company.

We have a small cleaning company, our main focus is car detailing but we are also expanding to home and residential cleaning and power washing.
I would like the web site to have a simple layout and SEO friendly.
I would also like to have a contact page in which clients can contact us and upload pictures of the house or car so we can provide an estimate.
A Page that shows the services we offer.

Target Market(s)

High paying clients for car detailiing and focus on residential and commercial cleaning.

Industry/Entity Type

Cleaning Service

Coding

Coded - Design and coding required

Number of Pages Required

4 page

Font styles to use
Serif

Colors

Designer to choose only greyscale colors for use in the design.

Requirements
Must have
• A home page.
Blog page for SEO
Contact page with the choice of clients to upload theirs pictures so we can provide estimates with calendar integration so they can provide their available dates for service.
A pictures to sell our services.
Nice to have
• Simple but sleek desing, I am more interested in SEO Score than heavy loads

```html
<!DOCTYPE html>
<html lang="en">
<head>
<meta charset="utf-8">
<title>Harbor Line Mobile Detailing</title>
<link rel="stylesheet" href="https://fonts.googleapis.com/css2?family=Roboto+Slab:wght@400;500;700&family=Source+Serif+4:wght@400;500;600;700&display=swap">
<style>
:root{
  --accent:#1c1c1c;
  --accent-soft:#3a3a3a;
  --accent-mid:#707070;
  --ink:#222;
  --text:#555;
  --nav:#5a5a5a;
  --light:#f1f1f1;
  --dark:#262626;
  --panel:#222;
  --line:#ccc;
  --footer-head:#bdbdbd;
  --white:#fff;
}
*{box-sizing:border-box;margin:0;padding:0}
html,body{width:1200px;height:3900px;overflow:hidden}
body{position:relative;background:var(--white);font-family:'Source Serif 4',serif;color:var(--text)}
.abs{position:absolute}
.head-font{font-family:'Roboto Slab',serif}

/* header */
.topline{left:0;top:0;width:1200px;height:4px;background:var(--accent)}
.header{left:0;top:4px;width:1200px;height:132px;background:var(--white)}
.brand-box{left:73px;top:0;width:160px;height:178px;background:var(--white);z-index:3;display:flex;flex-direction:column;align-items:center;justify-content:center;gap:12px}
.brand-mark{width:44px;height:44px;background:var(--ink)}
.brand-name{font-family:'Roboto Slab',serif;font-weight:700;font-size:16px;line-height:20px;color:var(--ink);text-align:center;text-transform:uppercase}
.info{display:flex;align-items:center;gap:12px;font-size:14px;line-height:19px;color:var(--ink)}
.info b{display:block;font-weight:700;font-size:13px}
.social{display:flex;gap:8px}
.social span{width:27px;height:27px;border-radius:50%;background:var(--accent-soft)}
.social span.alt{background:var(--accent-mid)}
.nav{left:0;top:136px;width:1200px;height:42px;background:var(--nav)}
.nav ul{list-style:none;position:absolute;left:233px;top:0;height:42px;display:flex}
.nav li{height:42px;display:flex;align-items:center;justify-content:center;padding:0 22px;color:var(--white);font-size:13px;font-weight:500;border-right:1px solid #6d6d6d;text-transform:uppercase}
.nav li.active{background:var(--accent)}
.nav .book{left:924px;top:0;width:203px;height:42px;background:var(--accent);color:var(--white);font-size:16px;font-weight:600;display:flex;align-items:center;justify-content:center}

/* hero */
.hero{left:0;top:178px;width:1200px;height:539px;background:linear-gradient(100deg,#3b3b3b 0%,#8a8a8a 30%,#9c9c9c 55%,#5a5a5a 80%,#2f2f2f 100%)}
.hero-pre{left:502px;top:288px;color:var(--white);font-size:25px;letter-spacing:.5px}
.hero-title{left:500px;top:332px;color:var(--white);font-family:'Roboto Slab',serif;font-weight:700;font-size:38px}
.hero-text{left:502px;top:398px;width:620px;color:var(--white);font-size:19px;line-height:32px}
.dots{left:554px;top:666px;display:flex;gap:12px}
.dots span{width:20px;height:6px;background:var(--white)}
.dots span.on{background:var(--accent)}

/* common */
.eyebrow{font-family:'Roboto Slab',serif;font-weight:700;font-size:14px;color:var(--accent-soft);text-transform:uppercase}
.h2{font-family:'Roboto Slab',serif;font-weight:700;font-size:32px;color:#333;text-transform:uppercase}
.btn{display:flex;align-items:center;background:var(--accent);color:var(--white);font-size:14px;font-weight:600}
.btn .lbl{flex:1;padding-left:20px}
.btn .arrow{width:40px;height:100%;background:var(--accent-mid);clip-path:polygon(25% 0,100% 0,100% 100%,0 100%);display:flex;align-items:center;justify-content:center}
.centered-title{left:0;width:1200px;display:flex;align-items:center;justify-content:center;gap:14px}
.centered-title i{width:32px;height:3px;background:var(--accent)}
.photo{border-radius:2px}

/* about */
.about-text{left:73px;top:898px;width:543px;font-size:12.5px;line-height:26.3px;text-align:justify;color:var(--text)}
.rule{left:73px;top:864px;width:124px;height:3px;background:var(--accent)}
.frame-l{left:681px;top:826px;width:3px;height:339px;background:var(--line)}
.frame-r{left:1145px;top:875px;width:3px;height:340px;background:var(--line)}
.frame-b{left:1100px;top:1212px;width:48px;height:3px;background:var(--line)}
.frame-t{left:681px;top:826px;width:20px;height:3px;background:var(--line)}

/* services */
.services{left:0;top:1324px;width:1200px;height:1000px;background:var(--light)}
.svc-img{width:289px;height:194px}
.svc-bar{width:230px;height:7px;background:var(--accent)}
.svc-title{font-family:'Roboto Slab',serif;font-weight:700;font-size:18px;color:#222;text-transform:uppercase}
.svc-text{width:310px;font-size:12.5px;line-height:21px;color:var(--text)}

/* appointment */
.appt-photo{left:614px;top:2392px;width:513px;height:481px;background:linear-gradient(135deg,#4a4a4a,#8a8a8a 45%,#2a2a2a)}
.appt-panel{left:74px;top:2431px;width:636px;height:431px;background:var(--panel);border-radius:4px}
.appt-title{left:129px;top:2474px;font-family:'Roboto Slab',serif;font-weight:700;font-size:22px;color:var(--white)}
.field{background:var(--white);border-radius:2px;height:50px;display:flex;align-items:center;justify-content:space-between;padding:0 20px;font-size:15px;color:#666}
.field .browse{background:#e2e2e2;color:#333;font-size:13px;padding:6px 12px;border-radius:2px}

/* blog */
.blog-card{width:318px;height:426px;background:#f4f4f4}
.blog-img{width:318px;height:195px}
.blog-title{position:absolute;left:18px;top:214px;width:285px;font-size:16px;line-height:26px;font-weight:600;color:#222}
.blog-text{position:absolute;left:18px;top:270px;width:285px;font-size:14.5px;line-height:23.5px;color:var(--text)}
.blog-date{position:absolute;left:18px;top:355px;font-size:11.5px;color:#333}
.blog-btn{position:absolute;left:0;top:390px;width:318px;height:37px;background:linear-gradient(90deg,#2a2a2a,#1a1a1a 80%,#444);color:var(--white);display:flex;align-items:center;justify-content:center;font-size:14px}

/* footer */
.footer{left:0;top:3525px;width:1200px;height:375px;background:var(--dark)}
.f-brand{left:90px;top:3588px;width:115px;display:flex;flex-direction:column;align-items:center;gap:10px}
.f-brand .brand-mark{background:var(--white);width:38px;height:38px}
.f-brand .brand-name{color:var(--white);font-size:14px;line-height:18px}
.f-social{left:90px;top:3743px;display:flex;gap:16px}
.f-social span{width:28px;height:28px;border-radius:50%;border:2px solid var(--footer-head)}
.f-head{font-size:16px;font-weight:600;color:var(--footer-head)}
.f-list{list-style:none;font-size:13px;line-height:26.5px;color:var(--white)}
.f-contact{font-size:13px;line-height:23px;color:var(--white)}
.f-contact .row{display:flex;gap:10px}
.copy{left:0;top:3858px;width:1200px;text-align:center;font-size:13px;color:var(--white)}
</style>
</head>
<body>

<!-- header -->
<div class="abs topline"></div>
<div class="abs header"></div>
<div class="abs brand-box">
  <div class="brand-mark"></div>
  <div class="brand-name">Harbor Line<br>Mobile Detailing</div>
</div>
<div class="abs info" style="left:526px;top:54px">
  <svg width="34" height="34" viewBox="0 0 34 34" fill="none" stroke="#1c1c1c" stroke-width="2.4"><circle cx="17" cy="17" r="14"/><path d="M17 9v8l6 4"/></svg>
  <div><b>Opening Hours:</b>MON - SAT &nbsp;9:00 AM - 6:00 PM</div>
</div>
<div class="abs info" style="left:782px;top:50px">
  <svg width="34" height="34" viewBox="0 0 34 34" fill="none" stroke="#1c1c1c" stroke-width="2.4" stroke-linejoin="round"><path d="M8 4l6 7-3 4c2 4 5 7 9 9l4-3 7 6-4 4C16 31 3 18 4 8z"/></svg>
  <div><b>Call To:</b>(555) 014-2290</div>
</div>
<div class="abs social" style="left:992px;top:56px" aria-label="Social links">
  <span></span><span></span><span></span><span class="alt"></span>
</div>

<nav class="abs nav">
  <ul>
    <li class="active">Home</li>
    <li>About &nbsp;<svg width="9" height="6" viewBox="0 0 9 6"><path d="M1 1l3.5 3.5L8 1" stroke="#fff" fill="none" stroke-width="1.4"/></svg></li>
    <li>Detailing Service</li>
    <li>Gallery</li>
    <li>Reviews</li>
    <li style="border:none">Contact</li>
  </ul>
  <div class="abs book">BOOK OUR SERVICE</div>
</nav>

<!-- hero -->
<div class="abs hero" role="img" aria-label="Photo of a detailer spraying foam over a black car"></div>
<div class="abs hero-pre">WE PROVIDE</div>
<h1 class="abs hero-title">BEST QUALITY AUTO DETAILING</h1>
<p class="abs hero-text">Leading professional car care portal providing professional service at your doorstep, complete exterior and interior cleaning, car polish, decorative works and many more.</p>
<div class="abs dots"><span class="on"></span><span></span><span></span></div>

<!-- about -->
<div class="abs eyebrow" style="left:73px;top:783px">Welcome To</div>
<h2 class="abs h2" style="left:73px;top:806px">Harbor Line Mobile Detailing</h2>
<div class="abs rule"></div>
<p class="abs about-text">With a long and successful history in the Dalton, OR area, Ridgeview Auto Care Centers have three convenient locations to service your vehicle. We are a Full Service auto repair company offering comprehensive services and repairs for all makes and models of vehicles ranging from passenger cars and trucks to RVs to fleet vehicles. Each store specializes in tires from Roadmark®, TreadPoint®, Ironway® and many other brands. Our tire prices can compete with Bulkway and the Wheel Depot.<br>For your convenience, the gas pumps at all of our Ridgeview Auto Care locations are open 24/7. We offer packaged ApexRun racing fuel products for high performance street vehicles. Higher octane fuels for off road use are also available at all Ridgeview Auto Care locations. We are a local business serving local customers in Dalton and our surrounding communities. At Ridgeview Auto Care Centers we're passionate about our service!</p>
<div class="abs btn" style="left:73px;top:1224px;width:168px;height:40px">
  <span class="lbl">More About Us</span>
  <span class="arrow"><svg width="8" height="12" viewBox="0 0 8 12"><path d="M2 1l5 5-5 5" stroke="#fff" fill="none" stroke-width="1.6"/></svg></span>
</div>
<div class="abs head-font" style="left:723px;top:792px;font-size:17px;font-weight:700;color:#888">BEST SERVICES @ AFFORDABLE PRICE</div>
<div class="abs frame-l"></div><div class="abs frame-t"></div>
<div class="abs frame-r"></div><div class="abs frame-b"></div>
<div class="abs photo" style="left:698px;top:826px;width:431px;height:389px;background:linear-gradient(160deg,#a0a0a0,#6a6a6a 55%,#3a3a3a)" role="img" aria-label="Photo of a smiling mechanic in overalls holding a clipboard"></div>

<!-- services -->
<section class="abs services"></section>
<div class="abs eyebrow" style="left:0;width:1200px;text-align:center;top:1366px">What We Do</div>
<div class="abs centered-title" style="top:1388px"><i></i><h2 class="h2">Our Services</h2><i></i></div>

<div class="abs photo svc-img" style="left:73px;top:1484px;background:linear-gradient(135deg,#d8d8d8,#9a9a9a 50%,#4a4a4a)" role="img" aria-label="Photo of a car drying in the sunset"></div>
<div class="abs svc-bar" style="left:78px;top:1678px"></div>
<h3 class="abs svc-title" style="left:72px;top:1710px">Car Cleaning</h3>
<p class="abs svc-text" style="left:73px;top:1749px">Your vehicle's belts and hoses are involved in processes within the cooling system, air conditioning system, charging system, and engine...</p>

<div class="abs photo svc-img" style="left:443px;top:1484px;background:linear-gradient(135deg,#e8e8e8,#b9b9b9 55%,#707070)" role="img" aria-label="Photo of a white car being power washed"></div>
<div class="abs svc-bar" style="left:448px;top:1678px"></div>
<h3 class="abs svc-title" style="left:443px;top:1710px">Power Washing</h3>
<p class="abs svc-text" style="left:443px;top:1749px">A fully functioning brake system is crucial to your safety, the safety of your passengers, and the safety of other drivers on the road...</p>

<div class="abs photo svc-img" style="left:812px;top:1484px;background:linear-gradient(135deg,#555,#a8a8a8 50%,#e6e6e6)" role="img" aria-label="Photo of a cleaning bucket with brushes and a mop"></div>
<div class="abs svc-bar" style="left:817px;top:1678px"></div>
<h3 class="abs svc-title" style="left:811px;top:1710px">Residential Cleaning</h3>
<p class="abs svc-text" style="left:812px;top:1749px">Vehicle inspections help to regulate proper vehicle maintenance. They also contribute to safe driving conditions...</p>

<div class="abs photo svc-img" style="left:73px;top:1861px;background:linear-gradient(135deg,#3a3a3a,#9a9a9a 55%,#dcdcdc)" role="img" aria-label="Photo of a hand wiping a car interior with a cloth"></div>
<div class="abs svc-bar" style="left:78px;top:2055px"></div>
<h3 class="abs svc-title" style="left:73px;top:2087px">Interior Cleaning</h3>
<p class="abs svc-text" style="left:73px;top:2126px">An oil change and oil filter replacement are one of many preventative maintenance services that help promote maximum vehicle performance...</p>

<div class="abs photo svc-img" style="left:443px;top:1861px;background:linear-gradient(135deg,#2e2e2e,#828282 55%,#3c3c3c)" role="img" aria-label="Photo of a polishing pad applying ceramic coating"></div>
<div class="abs svc-bar" style="left:448px;top:2055px"></div>
<h3 class="abs svc-title" style="left:442px;top:2087px">Ceramic Coating</h3>
<p class="abs svc-text" style="left:443px;top:2126px">A wheel alignment consists of adjusting the wheels of your vehicle so that all wheels are parallel to each other and perpendicular to the ground...</p>

<div class="abs photo svc-img" style="left:812px;top:1861px;background:linear-gradient(135deg,#6f6f6f,#c9c9c9 50%,#3d3d3d)" role="img" aria-label="Photo of a worker buffing a car body with a polisher"></div>
<div class="abs svc-bar" style="left:817px;top:2055px"></div>
<h3 class="abs svc-title" style="left:817px;top:2087px">Paint Protection Film</h3>
<p class="abs svc-text" style="left:812px;top:2126px">Located on the underside of your vehicle, the exhaust system is responsible for collecting and directing harmful emissions away from...</p>

<div class="abs btn" style="left:516px;top:2224px;width:168px;height:40px">
  <span class="lbl">More Services</span>
  <span class="arrow"><svg width="8" height="12" viewBox="0 0 8 12"><path d="M2 1l5 5-5 5" stroke="#fff" fill="none" stroke-width="1.6"/></svg></span>
</div>

<!-- appointment -->
<div class="abs photo appt-photo" role="img" aria-label="Photo of a smiling mechanic in overalls holding a wrench beside an open engine"></div>
<div class="abs appt-panel"></div>
<h2 class="abs appt-title">SCHEDULE AN APPOINTMENT</h2>
<div class="abs field" style="left:130px;top:2528px;width:528px">Enter Your Name</div>
<div class="abs field" style="left:130px;top:2599px;width:257px">Contact Number</div>
<div class="abs field" style="left:399px;top:2599px;width:259px">Email Address</div>
<div class="abs field" style="left:130px;top:2669px;width:257px">Select Service
  <svg width="12" height="8" viewBox="0 0 12 8"><path d="M1 1l5 5 5-5" stroke="#888" fill="none" stroke-width="1.5"/></svg></div>
<div class="abs field" style="left:399px;top:2669px;width:259px">Schedule Date
  <svg width="20" height="20" viewBox="0 0 20 20" fill="none" stroke="#999" stroke-width="1.4"><rect x="2" y="4" width="16" height="14"/><path d="M2 8h16M6 2v4M14 2v4M6 11h2M10 11h2M14 11h1M6 14h2M10 14h2"/></svg></div>
<div class="abs field upload" style="left:130px;top:2739px;width:528px">
  <span style="display:flex;align-items:center;gap:10px"><svg width="18" height="18" viewBox="0 0 18 18" fill="none" stroke="#888" stroke-width="1.5"><path d="M9 12V3M5 7l4-4 4 4M2 12v3h14v-3"/></svg>Upload Photos of Car or Home</span>
  <span class="browse">Browse</span>
</div>
<div class="abs btn" style="left:130px;top:2804px;width:167px;height:40px">
  <span class="lbl" style="font-weight:700;font-size:15px">BOOK NOW</span>
  <span class="arrow"><svg width="8" height="12" viewBox="0 0 8 12"><path d="M2 1l5 5-5 5" stroke="#fff" fill="none" stroke-width="1.6"/></svg></span>
</div>

<!-- blog -->
<div class="abs eyebrow" style="left:0;width:1200px;text-align:center;top:2945px">How It Works</div>
<div class="abs centered-title" style="top:2969px"><i></i><h2 class="h2">Latest Blog</h2><i></i></div>

<article class="abs blog-card" style="left:73px;top:3046px">
  <div class="blog-img" style="background:linear-gradient(135deg,#2a2a2a,#8c8c8c 50%,#1e1e1e)" role="img" aria-label="Photo of a polisher buffing a car panel"></div>
  <h3 class="blog-title">Car Cleaning and Car Washing Service new Schedule</h3>
  <p class="blog-text">The Valley Hawks is back on the gridir on and Ridgeview Auto Care Centers back the pack! ..</p>
  <div class="blog-date">September 10, 2013 by Permalink</div>
  <div class="blog-btn">READ MORE</div>
</article>
<article class="abs blog-card" style="left:442px;top:3046px">
  <div class="blog-img" style="background:linear-gradient(135deg,#777,#4a4a4a 50%,#2a2a2a)" role="img" aria-label="Photo of a mechanic fitting a wheel onto a car"></div>
  <h3 class="blog-title">Shop Local. Buy Local. Pump Local.</h3>
  <p class="blog-text">As you shop this holiday season, remember to support local business. By shopping at locally owned businesses</p>
  <div class="blog-date">January 24, 2013 by Permalink</div>
  <div class="blog-btn">READ MORE</div>
</article>
<article class="abs blog-card" style="left:809px;top:3046px">
  <div class="blog-img" style="background:linear-gradient(135deg,#bdbdbd,#7e7e7e 50%,#424242)" role="img" aria-label="Photo of a man pressure washing a car outdoors"></div>
  <h3 class="blog-title">Discount Offer on new deals and packages</h3>
  <p class="blog-text">Since 1975, Ridgeview Auto Care Centers has provided outstanding sales and service for tires, wheels and quality..</p>
  <div class="blog-date">August 7, 2012 by Permalink</div>
  <div class="blog-btn">READ MORE</div>
</article>

<!-- footer -->
<footer class="abs footer"></footer>
<div class="abs f-brand">
  <div class="brand-mark"></div>
  <div class="brand-name">Harbor Line<br>Mobile Detailing</div>
</div>
<div class="abs f-social" aria-label="Social links"><span></span><span></span><span></span></div>

<div class="abs f-head" style="left:343px;top:3577px">Main Links</div>
<ul class="abs f-list" style="left:343px;top:3611px">
  <li>Home</li><li>About Us</li><li>Detailing Service</li><li>Gallery</li><li>Reviews</li><li>Contact Us</li>
</ul>
<div class="abs f-head" style="left:593px;top:3577px">Info Links</div>
<ul class="abs f-list" style="left:593px;top:3611px">
  <li>Latest Blog</li><li>Terms and Conditions</li><li>Privacy Policy</li>
</ul>
<div class="abs f-head" style="left:861px;top:3577px">Contact Us</div>
<div class="abs f-contact" style="left:861px;top:3614px">
  <div class="row"><svg width="14" height="16" viewBox="0 0 14 16"><path d="M7 1a5 5 0 015 5c0 4-5 9-5 9S2 10 2 6a5 5 0 015-5z" fill="#bdbdbd"/><circle cx="7" cy="6" r="2" fill="#262626"/></svg><span>212 Maple Row, Unit C,<br>Lakeview</span></div>
  <div class="row" style="margin-top:4px"><svg width="14" height="16" viewBox="0 0 14 16"><path d="M2 2l3 0 1.5 3.5-2 1.5c1 2 2 3 4 4l1.5-2L13 10.5V13c-6 1-12-5-11-11z" fill="#bdbdbd"/></svg><span>+1 555 018 3344<br>+1 555 017 6621</span></div>
  <div class="row" style="margin-top:4px"><svg width="16" height="16" viewBox="0 0 16 16"><rect x="1" y="3" width="14" height="10" fill="#bdbdbd"/><path d="M1 3l7 6 7-6" stroke="#262626" fill="none" stroke-width="1.3"/></svg><span>info@harborlinedetailing.com</span></div>
</div>
<div class="abs copy">Harbor Line Mobile Detailing © 2020. All Rights Reserved.</div>

</body>
</html>
```